Ward Compass Business Card Design*

We need a business card design for our company Ward Compass. Our company is specialized in providing online consulting services regarding medical institutions, hospitals and doctors. We work with patients worldwide looking to choose between healthcare providers. We have a website you may use as a reference, where we list doctors and clinics worldwide. So we target Medical providers as well as patients worldwide.
Target Market(s)
Medical Providers and patients around the world
Industry/Entity Type
Medical
Contact Information for Business Card
Salma Derkaoui
CEO
+90 612 348 2071
info@wardcompass-example.com
www.wardcompass-example.com
14 Annakhil 3 H.R.B. Rabat, Morocco
Requirements
Must have
- Company logo/name on one full side, personal info and smaller logo and company name on the other side.
Nice to have
- Smart and elegant design

```html
<!DOCTYPE html>
<html lang="en">
<head>
<meta charset="utf-8">
<title>Ward Compass – Business Card</title>
<link rel="stylesheet" href="https://fonts.googleapis.com/css2?family=Lato:wght@400;700&family=Montserrat:wght@600&display=swap">
<style>
  :root {
    --stage: #b5b5b5;
    --navy: #1d3a6b;
    --paper: #ffffff;
    --ink: #2a2a2a;
  }
  * { margin: 0; padding: 0; box-sizing: border-box; }
  html, body { width: 1154px; height: 1200px; overflow: hidden; background: var(--stage); }
  .canvas { position: relative; width: 1154px; height: 1200px; }

  .card { position: absolute; left: 163px; width: 806px; height: 458px; overflow: hidden; }
  .card--front { top: 94px; background: var(--navy); }
  .card--back { top: 590px; background: var(--paper); }

  .brand { position: absolute; display: flex; align-items: center; white-space: nowrap; }
  .brand__dot { border-radius: 50%; flex: none; }
  .brand__name { font-family: "Montserrat", sans-serif; font-weight: 600; text-transform: uppercase; }

  .card--front .brand { left: 157px; top: 196px; gap: 26px; }
  .card--front .brand__dot { width: 64px; height: 64px; background: var(--paper); }
  .card--front .brand__name { color: var(--paper); font-size: 44px; letter-spacing: 1px; }

  .card--back .brand { left: 61px; top: 210px; gap: 16px; }
  .card--back .brand__dot { width: 46px; height: 46px; background: var(--navy); }
  .card--back .brand__name { color: var(--navy); font-size: 28px; letter-spacing: 0.5px; }

  .divider { position: absolute; left: 402px; top: 114px; width: 2px; height: 231px; background: var(--navy); }

  .details { position: absolute; left: 429px; top: 110px; font-family: "Lato", sans-serif; color: var(--ink); }
  .details__name { font-weight: 700; font-size: 33px; line-height: 1; color: var(--navy); text-transform: uppercase; letter-spacing: -0.3px; }
  .details__role { font-size: 21px; line-height: 1; margin-top: 8px; }
  .details__address { font-size: 21px; line-height: 29px; margin-top: 16px; font-style: normal; }
  .contacts { list-style: none; margin-top: 12px; }
  .contacts li { display: flex; align-items: center; gap: 10px; font-size: 21px; line-height: 29px; }
  .contacts svg { width: 18px; height: 18px; flex: none; fill: var(--navy); }

  .band { position: absolute; left: 0; bottom: 0; width: 100%; height: 11px; background: var(--navy); }
</style>
</head>
<body>
<main class="canvas">
  <section class="card card--front" aria-label="Card front">
    <div class="brand">
      <span class="brand__dot"></span>
      <span class="brand__name">Ward Compass</span>
    </div>
  </section>

  <section class="card card--back" aria-label="Card back">
    <div class="brand">
      <span class="brand__dot"></span>
      <span class="brand__name">Ward Compass</span>
    </div>
    <div class="divider"></div>
    <div class="details">
      <h1 class="details__name">Salma Derkaoui</h1>
      <p class="details__role">CEO</p>
      <address class="details__address">14 Annakhil 3<br>H.R.B. Rabat, Morocco</address>
      <ul class="contacts">
        <li>
          <svg viewBox="0 0 24 24" aria-hidden="true"><path d="M6.6 10.8a15.1 15.1 0 0 0 6.6 6.6l2.2-2.2c.3-.3.7-.4 1-.2 1.1.4 2.3.6 3.6.6.6 0 1 .4 1 1V20c0 .6-.4 1-1 1A17 17 0 0 1 3 4c0-.6.4-1 1-1h3.5c.6 0 1 .4 1 1 0 1.3.2 2.5.6 3.6.1.3 0 .7-.2 1z"/></svg>
          <span>+90 612 348 2071</span>
        </li>
        <li>
          <svg viewBox="0 0 24 24" aria-hidden="true"><path d="M2 5h20v14H2zm2 2v.4l8 5.2 8-5.2V7z"/></svg>
          <span>info@wardcompass-example.com</span>
        </li>
        <li>
          <svg viewBox="0 0 24 24" aria-hidden="true"><path d="M12 2a10 10 0 1 0 0 20 10 10 0 0 0 0-20zm-1 17.9A8 8 0 0 1 4.1 10L9 15v1c0 1.1.9 2 2 2zm6.9-2.5A2 2 0 0 0 16 16h-1v-3c0-.6-.4-1-1-1H8v-2h2c.6 0 1-.4 1-1V7h2c1.1 0 2-.9 2-2v-.4a8 8 0 0 1 2.9 12.8z"/></svg>
          <span>www.wardcompass-example.com</span>
        </li>
      </ul>
    </div>
    <div class="band"></div>
  </section>
</main>
</body>
</html>
```